Business card design for QuelMarvion

I need a business card based on the logo design produced for QuelMarvion. The company is focused on triathlon and endurance sport coaching and the tag line is (per the logo) "Stamina. Focus. Progress". The design should be sophisticated, appropriate to an affluent and business oriented target market. Colors are optional but the color of the logo probably dictates the color used on the card. I envisage using the red logo, with black print for the wording and contact numbers on a white or cream background, but am open to alternative suggestions. I expect to select something fairly conventional, but would like to see some designs that are less conventional to stretch my thinking on what could be appropriate. I am assuming a single side design is best, but willing to consider double sided as an option.

Target Market(s)

Individual athletes and corporate health and wellness leaders

Industry/Entity Type

Health And Wellness

Contact Information for Business Card

The card should provide the following information:
Logo
My name: Gordon Lashby
Company website: QuelMarvion.com
My email: gordon.lashby@quelmarvion.com
My cell phone number: +1-555-018-2739

Font styles to use
Sans Serif

Colors

Designer to choose colors to be used in the design.

Requirements
Must have
• Space on the card - simple design, not over crowded.
Nice to have
• clean and clear font, nothing garish or mass market like
Should not have
• Do not add pictures

```html
<!DOCTYPE html>
<html lang="en">
<head>
<meta charset="utf-8">
<title>QuelMarvion Business Card</title>
<link rel="stylesheet" href="https://fonts.googleapis.com/css2?family=Open+Sans:wght@400;600;700&family=Saira+Semi+Condensed:wght@600&family=Questrial&display=swap">
<style>
  :root {
    --backdrop: #c8c8c8;
    --brand-red: #8b2623;
    --brand-red-dark: #7e211f;
    --card-white: #f4f4f4;
    --ink: #2a2a2a;
    --swoosh: #2e3338;
    --paper-text: #f3eeee;
  }
  * { margin: 0; padding: 0; box-sizing: border-box; }
  html, body {
    width: 1200px; height: 576px; overflow: hidden;
    background: var(--backdrop);
  }
  .canvas { position: relative; width: 1200px; height: 576px; }

  .card {
    position: absolute;
    border-radius: 14px;
    overflow: hidden;
  }

  /* Front */
  .card-front {
    left: 82px; top: 139px;
    width: 484px; height: 291px;
    background: linear-gradient(180deg, var(--brand-red) 0%, var(--brand-red-dark) 100%);
    color: var(--paper-text);
  }
  .front-wordmark {
    position: absolute; left: 0; right: 0; top: 138px;
    text-align: center;
    font-family: "Open Sans", sans-serif;
    font-weight: 600; font-size: 45px; line-height: 1;
    letter-spacing: -0.5px;
  }
  .front-tagline {
    position: absolute; left: 0; right: 0; top: 188px;
    text-align: center;
    font-family: "Open Sans", sans-serif;
    font-size: 15px; letter-spacing: 1px;
  }

  /* Back */
  .card-back {
    left: 602px; top: 138px;
    width: 480px; height: 290px;
    background: linear-gradient(160deg, #fbfbfb 0%, var(--card-white) 60%, #e9e9e9 100%);
  }
  .card-wave { position: absolute; left: 0; top: 0; width: 480px; height: 290px; }

  .holder-name {
    position: absolute; left: 28px; top: 40px;
    font-family: "Saira Semi Condensed", sans-serif;
    font-weight: 600; font-size: 20px; line-height: 1.2; color: var(--brand-red);
  }
  .holder-role {
    position: absolute; left: 28px; top: 71px;
    font-family: "Questrial", sans-serif;
    font-size: 11.5px; color: var(--ink);
  }
  .back-wordmark {
    position: absolute; right: 24px; top: 60px;
    font-family: "Open Sans", sans-serif;
    font-weight: 600; font-size: 33px; line-height: 1;
    color: var(--brand-red); letter-spacing: -0.4px;
  }
  .back-tagline {
    position: absolute; right: 24px; top: 99px;
    font-family: "Open Sans", sans-serif;
    font-size: 10.5px; color: var(--ink); letter-spacing: 0.8px;
  }

  .contact-list {
    position: absolute; left: 28px; top: 166px;
    list-style: none;
    font-family: "Questrial", sans-serif;
    font-size: 13.5px; color: var(--ink);
  }
  .contact-list li { display: flex; align-items: center; height: 18.5px; }
  .contact-list svg { width: 11px; height: 11px; margin-right: 11px; fill: var(--brand-red); }
  .contact-list .accent { color: var(--brand-red); }

  .values-list {
    position: absolute; right: 24px; top: 217px;
    list-style: none; text-align: right;
    font-family: "Questrial", sans-serif;
    font-size: 14px; line-height: 18px; color: var(--paper-text);
  }
</style>
</head>
<body>
<main class="canvas">

  <section class="card card-front" aria-label="Card front">
    <div class="front-wordmark">QuelMarvion</div>
    <div class="front-tagline">STAMINA. FOCUS. PROGRESS</div>
  </section>

  <section class="card card-back" aria-label="Card back">
    <svg class="card-wave" viewBox="0 0 480 290" aria-hidden="true">
      <path d="M0,268 C100,292 200,290 300,246 C370,214 420,190 480,182 L480,290 L0,290 Z" fill="#8b2623"/>
      <path d="M0,248 C110,268 200,266 290,224 C360,192 420,172 480,164 L480,177 C420,185 360,205 298,236 C210,278 110,284 0,260 Z" fill="#2e3338"/>
    </svg>

    <div class="holder-name">Gordon Lashby</div>
    <div class="holder-role">Managing Director</div>

    <div class="back-wordmark">QuelMarvion</div>
    <div class="back-tagline">STAMINA. FOCUS. PROGRESS</div>

    <ul class="contact-list">
      <li>
        <svg viewBox="0 0 12 12" aria-hidden="true"><path d="M1,4 C1,2 3,1 6,1 C9,1 11,2 11,4 L9,5 L8,3.5 L4,3.5 L3,5 Z M2.5,6 L9.5,6 L10.5,11 L1.5,11 Z"/></svg>
        gordon.lashby@quelmarvion.com
      </li>
      <li>
        <svg viewBox="0 0 12 12" aria-hidden="true"><path d="M0.5,2.5 L11.5,2.5 L11.5,9.5 L0.5,9.5 Z"/><path d="M0.5,2.5 L6,7 L11.5,2.5" stroke="#f4f4f4" stroke-width="1" fill="none"/></svg>
        www.<span class="accent">QuelMarvion</span>.com
      </li>
      <li>
        <svg viewBox="0 0 12 12" aria-hidden="true"><circle cx="6" cy="6" r="5.5"/><path d="M0.5,6 L11.5,6 M6,0.5 L6,11.5 M6,0.5 C3,3 3,9 6,11.5 M6,0.5 C9,3 9,9 6,11.5" stroke="#f4f4f4" stroke-width="0.8" fill="none"/></svg>
        +1-555-018-2739
      </li>
    </ul>

    <ul class="values-list">
      <li>Stamina «</li>
      <li>Focus «</li>
      <li>Progress «</li>
    </ul>
  </section>

</main>
</body>
</html>
```